Lumora Website

I need a design of homepage for a health and wellness center. We considers self to be young and fresh and want something along that design. We want a main picture/logo/design (or all three), and underneath that 4 pictures to depict what services we do. The four services are Orthopedic Rehab, Neurological Rehab, Speech Pathology and Float. I have attached our logo, and some pictures that might be helpful, but the pictures don't have to be included. Here is an example of what I would like it look. http://pixelbazaar.example/web-design/contests/brightloop-website-design-needed-more-work-come-submit-519063/entries/74820615

Industry/Entity Type

Health

```html
<!DOCTYPE html>
<html lang="en">
<head>
<meta charset="utf-8">
<title>Lumora Center for Health + Wellness</title>
<link href="https://fonts.googleapis.com/css2?family=Bebas+Neue&family=Open+Sans:ital,wght@0,400;0,600;1,600;1,700&display=swap" rel="stylesheet">
<style>
:root{
  --lime:#8fb41f;
  --olive:#a9b159;
  --teal:#83b1a5;
  --teal-text:#6fa394;
  --ink:#3d3d3d;
  --footer:#262626;
  --line:#e3e3e3;
  --white:#ffffff;
}
*{margin:0;padding:0;box-sizing:border-box}
html,body{width:979px;height:1200px;overflow:hidden;background:var(--white)}
body{position:relative;font-family:"Open Sans",sans-serif;color:var(--ink)}
.display{font-family:"Bebas Neue",sans-serif;font-weight:400;letter-spacing:.5px}

/* header */
.site-header{position:absolute;left:0;top:0;width:979px;height:49px;background:var(--white);z-index:5}
.brand{position:absolute;left:183px;top:12px;display:flex;align-items:center;gap:7px}
.brand-mark{width:20px;height:20px;border-radius:50%;background:var(--lime)}
.brand-name{font-size:22px;font-weight:400;color:var(--teal-text);line-height:1}
.main-nav{position:absolute;left:591px;top:0;display:flex;height:49px}
.main-nav a{display:flex;align-items:center;justify-content:center;height:49px;font-size:7.5px;font-weight:600;color:var(--lime);text-decoration:none;border-left:1px solid var(--line);letter-spacing:.3px}
.main-nav a:last-child{border-right:1px solid var(--line)}
.main-nav .active{border-bottom:4px solid var(--olive);padding-top:4px}
.dropdown{position:absolute;left:636px;top:55px;width:91px;background:var(--white);box-shadow:0 1px 4px rgba(0,0,0,.15);z-index:6}
.dropdown a{display:block;height:23px;line-height:23px;padding-left:11px;font-size:7.5px;color:var(--lime);text-decoration:none;border-bottom:1px solid var(--line)}
.dropdown a:last-child{border-bottom:0}

/* hero */
.hero-photo{position:absolute;left:0;top:49px;width:979px;height:412px;background:linear-gradient(135deg,#d7dfe2 0%,#b9c3cc 45%,#c9ccd0 70%,#aeb6bf 100%)}
.hero-title{position:absolute;left:0;width:979px;top:249px;text-align:center;font-size:30px;color:var(--white)}
.hero-sub{position:absolute;left:0;width:979px;top:277px;text-align:center;font-size:9px;font-style:italic;font-weight:700;color:var(--white);padding-left:90px}
.hero-button{position:absolute;left:437px;top:299px;width:103px;height:25px;background:var(--white);border-bottom:3px solid var(--olive);font-size:7px;font-weight:600;letter-spacing:.6px;display:flex;align-items:center;justify-content:center;color:var(--ink)}
.hero-arrow{position:absolute;top:242px;width:16px;height:16px;border:1px solid var(--white);border-radius:50%}
.hero-dots{position:absolute;left:467px;top:420px;display:flex;gap:2px}
.hero-dots span{width:8px;height:8px;border:1px solid var(--white);border-radius:50%}
.hero-dots .on{background:var(--lime)}

.band{position:absolute;left:0;width:979px}

/* services */
.section-title{position:absolute;left:0;width:979px;text-align:center}
.services-title{top:495px;font-size:26px;color:var(--white)}
.service{position:absolute;top:557px;width:125px;color:var(--white)}
.service h3{font-family:"Bebas Neue",sans-serif;font-weight:400;font-size:15px;letter-spacing:.3px;line-height:18px}
.service p{font-size:8.4px;line-height:12.3px;margin-top:2px}
.learn-more{position:absolute;width:73px;height:23px;background:var(--white);border-bottom:2px solid #9fc9bc;font-size:7px;font-weight:600;color:var(--teal-text);display:flex;align-items:center;justify-content:center;letter-spacing:.3px}
.divider{position:absolute;top:561px;width:1px;height:141px;background:rgba(255,255,255,.35)}

/* about */
.about-title{top:757px;font-size:26px;color:var(--lime)}
.about-text{position:absolute;left:320px;top:800px;width:338px;font-size:7.6px;line-height:12.3px;text-align:justify;color:#444}

/* contact */
.contact-title{top:918px;font-size:16px;color:var(--white)}
.contact-form label{position:absolute;left:420px;font-size:8px;color:var(--white)}
.contact-form .field{position:absolute;left:418px;width:141px;background:var(--white);border-radius:2px}
.send{position:absolute;left:457px;top:1121px;width:60px;height:20px;background:var(--white);font-size:7px;font-weight:600;color:var(--teal-text);display:flex;align-items:center;justify-content:center;letter-spacing:.5px}

/* footer */
.site-footer{position:absolute;left:0;top:1155px;width:979px;height:45px;background:var(--footer)}
.copyright{position:absolute;left:183px;top:18px;font-size:6.5px;color:#cfcfcf}
.footer-nav{position:absolute;left:0;width:979px;top:18px;text-align:center;font-size:7px;font-weight:400;color:#e8e8e8;letter-spacing:.3px}
.social{position:absolute;left:628px;top:10px;display:flex;gap:5.5px}
.social span{width:23px;height:23px;border:1.5px solid #d8d8d8;border-radius:50%}
</style>
</head>
<body>

<header class="site-header">
  <div class="brand">
    <span class="brand-mark"></span>
    <span class="brand-name">Lumora</span>
  </div>
  <nav class="main-nav">
    <a style="width:46px">HOME</a>
    <a class="active" style="width:54px">SERVICES</a>
    <a style="width:48px">ABOUT</a>
    <a style="width:57px">CONTACT</a>
  </nav>
</header>
<nav class="dropdown">
  <a>Orthopedic Rehab</a>
  <a>Neurological Rehab</a>
  <a>Speech Pathology</a>
  <a>Float</a>
</nav>

<section class="hero">
  <div class="hero-photo" role="img" aria-label="Bright rehabilitation gym with exercise machines, parallel bars and a therapist working with a patient"></div>
  <span class="hero-arrow" style="left:183px"></span>
  <span class="hero-arrow" style="left:777px"></span>
  <h1 class="hero-title display">Our great slogan is over here</h1>
  <div class="hero-sub">slogan subline goes right here</div>
  <div class="hero-button">GET IN TOUCH</div>
  <div class="hero-dots"><span class="on"></span><span></span><span></span><span></span><span></span></div>
</section>

<svg class="band" style="top:428px" width="979" height="285" viewBox="0 0 979 285">
  <polygon points="0,0 489,33 979,0 979,257 489,284 0,257" fill="var(--olive)"/>
</svg>

<section class="services">
  <h2 class="section-title services-title display">Services</h2>
  <div class="service" style="left:199px"><h3>Orthopedic Rehab</h3><p>Lorem ipsum dolor sit amet, consectetur adipisicing elit, sed do eiusmod tempor incididunt ut labore et dolore magna aliqua.</p></div>
  <div class="service" style="left:355px"><h3>Neurological Rehab</h3><p>Lorem ipsum dolor sit amet, consectetur adipisicing elit, sed do eiusmod tempor incidi-<br>dunt ut labore et dolore magna aliqua.</p></div>
  <div class="service" style="left:506px"><h3>Speech Pathology</h3><p>Lorem ipsum dolor sit amet, consectetur adipisicing elit, sed do eiusmod tempor incididunt ut labore et dolore magna aliqua.</p></div>
  <div class="service" style="left:662px"><h3>Float</h3><p>Lorem ipsum dolor sit amet, consectetur adipisicing elit, sed do eiusmod tempor incidi-<br>dunt ut labore et dolore magna aliqua.</p></div>
  <div class="learn-more" style="left:199px;top:647px">LEARN MORE</div>
  <div class="learn-more" style="left:355px;top:649px">LEARN MORE</div>
  <div class="learn-more" style="left:506px;top:647px">LEARN MORE</div>
  <div class="learn-more" style="left:662px;top:647px">LEARN MORE</div>
  <span class="divider" style="left:336px"></span>
  <span class="divider" style="left:489px"></span>
  <span class="divider" style="left:642px"></span>
</section>

<section class="about">
  <h2 class="section-title about-title display">About</h2>
  <p class="about-text">Lorem ipsum dolor sit amet, consectetur adipisicing elit, sed do eiusmod tempor incididunt ut labore et dolore magna aliqua. Ut enim ad minim veniam, quis nostrud exercitation ullamco laboris nisi ut aliquip ex ea commodo consequat. Duis aute irure dolor in reprehenderit in voluptate velit esse cillum dolore eu fugiat nulla pariatur. Excepteur sint occaecat cupidatat non proident, sunt in culpa qui officia deserunt mollit anim id est laborum.</p>
</section>

<svg class="band" style="top:879px" width="979" height="277" viewBox="0 0 979 277">
  <polygon points="0,0 489,27 979,0 979,277 0,277" fill="var(--teal)"/>
</svg>

<section class="contact-form">
  <h2 class="section-title contact-title display">Get in touch</h2>
  <label style="top:943px">Name:</label>
  <div class="field" style="top:954px;height:21px"></div>
  <label style="top:979px">Email:</label>
  <div class="field" style="top:990px;height:20px"></div>
  <label style="top:1013px">Phone:</label>
  <div class="field" style="top:1024px;height:21px"></div>
  <label style="top:1047px">Message:</label>
  <div class="field" style="top:1058px;height:52px"></div>
  <div class="send">SEND</div>
</section>

<footer class="site-footer">
  <div class="copyright">©2014 Lumora. All Rights Reserved</div>
  <div class="footer-nav">HOME | SERVICES | ABOUT | CONTACT</div>
  <div class="social"><span></span><span></span><span></span><span></span><span></span><span></span></div>
</footer>

</body>
</html>
```